Business Card for Web Design consulting firm

Business card designs for Web Design consulting firm

Target Market(s)

English speaking adults ages 30 - 60. Predominantly professional services eg. Doctor, Dentist

Industry/Entity Type

Consulting

Requirements
Must have
• Double sided card

```html
<!DOCTYPE html>
<html lang="en">
<head>
<meta charset="utf-8">
<title>Lumora Business Card</title>
<link rel="stylesheet" href="https://fonts.googleapis.com/css2?family=Quicksand:wght@700&display=swap">
<style>
  :root {
    --card-white: #ffffff;
    --card-steel: #8e919a;
    --card-slate: #4c4e54;
    --card-bronze: #8a6431;
    --card-orange: #f69a1e;
    --brand-grey: #545559;
    --brand-orange: #f7a021;
    --ink: #0b0b0b;
    --ink-shadow: rgba(40, 40, 40, 0.7);
    --gold: #ffc400;
    --gold-shadow: #2b2416;
    --headline: #f2f2f2;
    --headline-shadow: #1e1f22;
  }
  * { margin: 0; padding: 0; box-sizing: border-box; }
  html, body {
    width: 1200px;
    height: 865px;
    overflow: hidden;
  }
  body {
    font-family: "Quicksand", "Varela Round", sans-serif;
    font-weight: 700;
  }
  .business-card {
    position: relative;
    width: 1200px;
    height: 865px;
    overflow: hidden;
    background: linear-gradient(152deg,
      var(--card-white) 0%,
      var(--card-white) 8%,
      var(--card-steel) 24%,
      var(--card-slate) 44%,
      var(--card-slate) 52%,
      var(--card-bronze) 72%,
      var(--card-orange) 100%);
  }
  .brand {
    position: absolute;
    left: 66px;
    top: 140px;
    width: 330px;
    display: flex;
    align-items: center;
    gap: 14px;
  }
  .brand-dot {
    flex: none;
    width: 40px;
    height: 40px;
    border-radius: 50%;
    background: var(--brand-orange);
  }
  .brand-name {
    font-size: 60px;
    line-height: 1;
    letter-spacing: 2px;
    color: var(--brand-grey);
  }
  .website {
    position: absolute;
    left: 78px;
    top: 236px;
    font-size: 30px;
    line-height: 1;
    color: var(--ink);
  }
  .tagline {
    position: absolute;
    left: 424px;
    top: 100px;
    font-size: 58px;
    line-height: 1;
    color: var(--headline);
    text-shadow: 4px 4px 0 var(--headline-shadow);
  }
  .person-name {
    position: absolute;
    left: 0;
    right: 90px;
    top: 322px;
    text-align: center;
    font-size: 106px;
    line-height: 1;
    color: var(--ink);
    text-shadow: 6px 6px 0 var(--ink-shadow);
  }
  .contact {
    color: var(--gold);
    font-size: 43px;
    line-height: 1;
    text-shadow: 3px 3px 0 var(--gold-shadow);
  }
  .address {
    position: absolute;
    left: 72px;
    top: 545px;
    font-style: normal;
  }
  .address-line { display: block; margin-bottom: 14px; }
  .phone {
    position: absolute;
    left: 72px;
    top: 748px;
  }
  .email {
    position: absolute;
    right: 75px;
    top: 748px;
  }
</style>
</head>
<body>
  <main class="business-card">
    <div class="brand">
      <span class="brand-dot"></span>
      <span class="brand-name">LUMORA</span>
    </div>
    <p class="website">www.lumoraweb.com</p>
    <h2 class="tagline">Web Design Consultancy</h2>
    <h1 class="person-name">Joseph Bloggs</h1>
    <address class="address contact">
      <span class="address-line">address line 1</span>
      <span class="address-line">address line 2</span>
      <span class="address-line">address line 3</span>
    </address>
    <p class="phone contact">Tel: 01234 567890</p>
    <p class="email contact">email: name@lumoraweb.com</p>
  </main>
</body>
</html>
```